Sustainable & Premier Artisan Jerky Makers (Custom Package / Label)

Use an earthy color for the background for all bags. Each animal logo should be it's own separate color. A bottom band going across in different colors can differentiate between all the different flavors. Traditional should be dark charcoal and other colors should be earthy. For the animals, use natural green, orange, red and blue. Colors for things that you would see naturally in the outdoors. They should work together in harmony and not clash. Animal icons should be rugged, bold and distinctive yet playful and inviting. Each animal should be it's own color.

This project will be guaranteed once we receive 1-2 samples that closely match our criteria and expectations. Our last logo project was completed for $900 after it was guaranteed. We will provide regular feedback and suggested improvements. Thank you.

We need a new front & back package design for our artisan jerky. The main part of the front of the package should be easily transferred to a label 3.5" x 5" which will be applied to a clear bag.

Please visit and browse our website for more information: www.vornelbrisk.example. We highly suggested you get acquainted with our brand and market positioning. Also, you can visit our SOCIAL MEDIA to get an idea: FB, Twitter, Instagram, Tumblr, Pinterest, etc. Our handle is "VORNELBRISK"

Logo Fonts:
Vornel Brisk = Hamburger Heaven
Greet Your Hungry Side & Purveyors of Choice Artisan Jerky = Champion HTF Featherweight

We make bison, beef, pork and turkey jerky from scratch for individuals leading active and healthy lifestyles. Our products are extremely high-end., e.g. each 2oz bag retails for $10+. We don't use any added sugar and have 8x less sodium.

We offer two (2) STYLES: (i) Rip Tear and (2) Soft Chew;
Of four (4) MEAT types: a) Bison, b) Beef. c) Pork and d) Turkey;
In five (5) gourmet FLAVORS: 1) Traditional (smoked), 2) Peppered, 3) Spicy 4) Guajillo Chile and 5) Asian Sesame

We need one package style. Attached are sample fonts we would like to use for the Rip Tear and Soft Chew STYLES (perhaps bags in different colors). We would like to show an illustration of the MEAT TYPE and FLAVOR on each bag. Note: These animal and flavor icons can be simple substitutes. Attached are samples of what we have been previously using.

About Vornel Brisk - The Next Great Artisan Meat Snacks Company

Vornel Brisk is a new kind of sustainable artisan meat snacks company. We are bringing back Classic Home Style, Rip Tear & Soft Chew Jerky handcrafted for individuals leading active and healthy lifestyles. Vornel Brisk are Purveyors of Choice Artisan Jerky made responsibly from scratch using real fruit and without any refined sugars, additives, non-natural flavorings or preservatives.

Vornel Brisk is 100% Paleo / Primal, Gluten-free and Certified Raw.

A revolutionary jerky and unlike any other on the market today, Vornel Brisk pairs perfectly with craft beers, wines & spirits and is preferred by outdoor recreationalists and performance athletes as well as beer lovers and foodies alike.

Thank you very much for your submissions.
Updates

Logo vectors have been uploaded as well as font typefaces for logo.

Logo Fonts:

Thank you all for your contributions thus far. Here is an update.

Please resubmit variations of your designs using use an earthy color for the background for all bag labels. The bag itself should be clear. Each animal logo should be it's own separate color. For the animals, use natural green, orange, red and blue. Colors for things that you would see naturally in the outdoors. They should work together in harmony and not clash. Animal icons should be rugged, bold and distinctive yet playful and inviting. Again, each animal should be it's own color. A bottom band going across in different colors can differentiate between all the different flavors. Traditional should be dark charcoal and other colors should be earthy.

Our team is llooking forward to seeing these next turns. Thank you very much.

Reason: Extending project deadline so we can hone in on the current submissions and get to a final product closer to meeting our packaging needs.

Target Market(s)

Outdoor recreationalists: Hikers, backpackers, rock climbers, hunters, etc.
Performance and recreational athletes: CrossFitters, triathletes, cyclists, weightlifters, runners, skiers, etc.
Foodies & aficionados: Gourmands and people who love high-end artisanal foods
Beverage connoisseurs: Craft beer, fine wine and refined spirit (scotch, whiskey, brandy, cognac) lovers

Industry/Entity Type

It Company

Requirements
Must have
• STYLES: (i) Rip Tear vs. (2) Soft Chew
(See attached sample fonts)

MEAT TYPE: a) Bison, b) Beef. c) Pork and d) Turkey
(See attached sample animal icons - these can re-illustrated to match our style or the bison can simply be made to match). Each animal type should be in its own respective color as per the attached.

GOURMET FLAVOR: 1) Traditional (smoked), 2) Peppered, 3) Spicy 4) Guajillo Chile and 5) Asian Sesame. These are simple word substitutes perhaps with matching icons or complementary silhouettes.

We need to incorporate some of these words / elements in a simple and straightforward way that will resonate with our target customers. Our focus is on "All natural, low carb and no added sugar".

"Your Lifestyle. Your Choice.
Classic Home Style.
Rip Tear. Artisan Jerky.
Real Food. By Real People.
All Natural. Low Carb.
Real Meat. Real Flavor.
No Sugar Added. Low Sodium.
Not Sticky. Non-greasy. Gristle-free.
Guilt-free. Delicious. Nutritious."
Nice to have
• Fonts for STYLES:
Rip Tear = Punk Rock Show
Soft Chew = Payday

"Oregon Made" and / or with Oregon map on the package front or back. See attached sample map.

Elements of a niche, specialty, high-end brand looking to attract loyal customers based on our fit with their active and healthy lifestyle. We are not chasing the one-off customer or the absolute dollar. Our company offers a lifestyle brand and products crafted for individuals with sophisticated tastes. These core traits should be included in the packaging which can have a combination of a retro & throwback / modern look and feel.

Focus should be on high-end customers who are interested in Talvenrock, GPX, Pellwick Hadley, etc. Focus on high-end athletics & outdoors with a mix of food and beverage.
Should not have
• Anything low-end, cheesy or chincy. Packaging should NOT resemble Dunto Jerky.

```html
<!DOCTYPE html>
<html lang="en">
<head>
<meta charset="utf-8">
<title>Vornel Brisk — Pork Peppered Labels</title>
<link href="https://fonts.googleapis.com/css2?family=Oswald:wght@400;600;700&family=Permanent+Marker&display=swap" rel="stylesheet">
<style>
  :root {
    --page: #ffffff;
    --label-red: #c95c57;
    --band-teal: #0d5a4f;
    --cream: #fbd9c6;
    --claim-pink: #f7a99b;
    --white: #ffffff;
    --soft-chew: #3a5a9e;
    --rip-tear: #e5204a;
    --pig-orange: #f49a5c;
    --pig-line: #e8772e;
    --muted: #9a9a9a;
    --divider: #dcdcdc;
  }
  * { box-sizing: border-box; margin: 0; padding: 0; }
  html, body { width: 1200px; height: 1200px; overflow: hidden; background: var(--page); }
  body { position: relative; font-family: "Oswald", sans-serif; }

  .label {
    position: absolute; left: 410px; width: 388px; height: 272px;
    background: var(--white); padding: 5px;
  }
  .label--soft { top: 132px; }
  .label--rip { top: 572px; }
  .label__field {
    position: relative; width: 100%; height: 100%;
    background: linear-gradient(170deg, var(--label-red) 0%, #d0665c 50%, var(--label-red) 100%);
    overflow: hidden;
  }
  .style-tag {
    position: absolute; left: 18px; top: 20px;
    transform: rotate(-6deg); text-align: center; line-height: 0.95;
  }
  .style-tag--soft {
    background: var(--soft-chew); color: var(--white);
    font-family: "Oswald", sans-serif; font-weight: 400; font-size: 24px;
    padding: 4px 6px; letter-spacing: 1px;
  }
  .style-tag--rip {
    color: var(--white); background: var(--rip-tear);
    font-family: "Permanent Marker", cursive; font-size: 21px; padding: 3px 6px;
  }
  .claims {
    position: absolute; right: 14px; top: 14px; transform: rotate(-5deg);
    color: var(--claim-pink); font-weight: 600; font-size: 11px;
    line-height: 1.35; text-transform: uppercase; letter-spacing: 0.3px;
  }
  .brand {
    position: absolute; left: 0; right: 0; top: 72px;
    display: flex; align-items: center; justify-content: center; gap: 10px;
  }
  .brand__dot { width: 20px; height: 20px; border-radius: 50%; background: var(--white); }
  .brand__name { color: var(--white); font-weight: 700; font-size: 40px; letter-spacing: 0.5px; }
  .tagline {
    position: absolute; left: 24px; top: 150px; transform: rotate(-4deg);
    color: var(--cream); font-weight: 700; font-size: 24px; line-height: 1.2;
    text-transform: uppercase; letter-spacing: 0.3px; white-space: nowrap;
  }
  .meat-icon {
    position: absolute; right: 44px; top: 190px; width: 32px; height: 30px;
    border-radius: 50% 50% 45% 45%; background: radial-gradient(circle at 45% 45%, #f7ab84, #ea8260);
  }
  .weight {
    position: absolute; right: 8px; top: 204px; line-height: 16px;
    color: var(--cream); font-weight: 600; font-size: 11px; white-space: nowrap;
  }
  .flavor-band {
    position: absolute; left: 0; right: 0; bottom: 0; height: 36px;
    background: var(--band-teal); display: flex; align-items: center; justify-content: center;
  }
  .flavor-band__name {
    color: var(--white); font-weight: 700; font-size: 21px; text-transform: uppercase;
  }

  .mascot {
    position: absolute; left: 104px; top: 952px; width: 176px; height: 192px;
    border-radius: 46% 46% 50% 50%;
    background: radial-gradient(circle at 50% 55%, #f6a872, var(--pig-orange) 60%, var(--pig-line));
  }

  .legend { position: absolute; left: 0; top: 0; width: 1200px; height: 1200px; pointer-events: none; }
  .divider { position: absolute; top: 932px; width: 1px; height: 234px; background: var(--divider); }
  .swatch { position: absolute; width: 44px; height: 42px; }
  .vlabel {
    position: absolute; transform: rotate(-90deg); transform-origin: left bottom;
    font-size: 9px; font-weight: 600; text-transform: uppercase; white-space: nowrap;
  }
  .group-title {
    position: absolute; top: 1148px; color: var(--muted);
    font-weight: 600; font-size: 15px; text-transform: uppercase; letter-spacing: 0.3px;
  }
  .animal {
    position: absolute; top: 944px; width: 42px; height: 40px; border-radius: 50%;
  }
</style>
</head>
<body>

  <section class="label label--soft">
    <div class="label__field">
      <div class="style-tag style-tag--soft">SOFT<br>CHEW</div>
      <div class="claims">Not Sticky<br>Non-Greasy<br>Gristle-Free</div>
      <div class="brand"><span class="brand__dot"></span><span class="brand__name">Vornel Brisk</span></div>
      <div class="tagline">Your Lifestyle. Your Choice.</div>
      <div class="meat-icon" role="img" aria-label="Pork icon: orange pig head"></div>
      <div class="weight">2.0 oz</div>
      <div class="flavor-band"><span class="flavor-band__name">Pork Peppered</span></div>
    </div>
  </section>

  <section class="label label--rip">
    <div class="label__field">
      <div class="style-tag style-tag--rip">RIP<br>TEAR</div>
      <div class="claims">Not Sticky<br>Non-Greasy<br>Gristle-Free</div>
      <div class="brand"><span class="brand__dot"></span><span class="brand__name">Vornel Brisk</span></div>
      <div class="tagline">Your Lifestyle. Your Choice.</div>
      <div class="meat-icon" role="img" aria-label="Pork icon: orange pig head"></div>
      <div class="weight">2.0 oz</div>
      <div class="flavor-band"><span class="flavor-band__name">Pork Peppered</span></div>
    </div>
  </section>

  <div class="mascot" role="img" aria-label="Large orange pig head illustration for the pork meat type"></div>

  <div class="legend">
    <div class="divider" style="left:562px"></div>
    <div class="divider" style="left:856px"></div>

    <span class="vlabel" style="left:476px;top:1072px;color:var(--soft-chew)">Soft Chew</span>
    <span class="vlabel" style="left:534px;top:1072px;color:var(--rip-tear)">Rip Tear</span>
    <div class="swatch" style="left:448px;top:1094px;background:var(--soft-chew)"></div>
    <div class="swatch" style="left:506px;top:1094px;background:var(--rip-tear)"></div>
    <div class="group-title" style="left:449px">Two Styles</div>

    <span class="vlabel" style="left:601px;top:1018px;color:#e2cfc1">Traditional (Smoked)</span>
    <span class="vlabel" style="left:658px;top:1018px;color:#f7c9e3">Spicy</span>
    <span class="vlabel" style="left:714px;top:1018px;color:#eaa9b8">Guajillo Chile</span>
    <span class="vlabel" style="left:771px;top:1018px;color:#fbdcc0">Asian Sesame</span>
    <span class="vlabel" style="left:827px;top:1018px;color:#076055">Peppered</span>
    <div class="swatch" style="left:573px;top:1040px;background:#e2cfc1"></div>
    <div class="swatch" style="left:630px;top:1040px;background:#f7c9e3"></div>
    <div class="swatch" style="left:686px;top:1040px;background:#f0b2c0"></div>
    <div class="swatch" style="left:743px;top:1040px;background:#fbdcc0"></div>
    <div class="swatch" style="left:799px;top:1040px;background:#076055"></div>
    <div class="swatch" style="left:573px;top:1094px;background:#ddc8b8"></div>
    <div class="swatch" style="left:630px;top:1094px;background:#f6c6e2"></div>
    <div class="swatch" style="left:686px;top:1094px;background:#eaa9b8"></div>
    <div class="swatch" style="left:743px;top:1094px;background:#f8d5bb"></div>
    <div class="swatch" style="left:799px;top:1094px;background:#00453c"></div>
    <div class="group-title" style="left:573px">Five Gourmet Flavors</div>

    <div class="animal" role="img" aria-label="Turkey icon in pink" style="left:871px;background:#f6b7c0"></div>
    <div class="animal" role="img" aria-label="Beef icon in mint" style="left:924px;background:#aee6df"></div>
    <div class="animal" role="img" aria-label="Pork icon in orange" style="left:983px;background:#f9a070"></div>
    <div class="animal" role="img" aria-label="Bison icon in lilac" style="left:1036px;background:#e0aee4"></div>
    <span class="vlabel" style="left:895px;top:1018px;color:#f6b7c0">Turkey</span>
    <span class="vlabel" style="left:952px;top:1018px;color:#aee6df">Beef</span>
    <span class="vlabel" style="left:1009px;top:1018px;color:#f9876c">Pork</span>
    <span class="vlabel" style="left:1066px;top:1018px;color:#e0aee4">Bison</span>
    <div class="swatch" style="left:867px;top:1040px;background:#f6b7c0"></div>
    <div class="swatch" style="left:924px;top:1040px;background:#aee6df"></div>
    <div class="swatch" style="left:981px;top:1040px;background:#f9876c"></div>
    <div class="swatch" style="left:1038px;top:1040px;background:#e0aee4"></div>
    <div class="swatch" style="left:867px;top:1094px;background:#dcaebb"></div>
    <div class="swatch" style="left:924px;top:1094px;background:#d4c6b5"></div>
    <div class="swatch" style="left:981px;top:1094px;background:#a3374b"></div>
    <div class="swatch" style="left:1038px;top:1094px;background:#d1b0b0"></div>
    <div class="group-title" style="left:867px">Four Meat Types</div>
  </div>

</body>
</html>
```